Three diagrams for an academic paper

I need professional-looking versions of three diagrams for an academic paper. I am uploading JPEGs of each diagram drafted in Vextra Docs. I need completely new versions that look much better.

Some detailed requirements:
- Professional styling - must be clearly superior to the ‘stick-figure’ example images and obviously not from powerpoint, etc.
- Must be a coordinated style across all three illustrations.
- Note that a mini-version of figure 2 appears in figure 3 (within the database image)
- I need very high resolution, suitable for a manuscript
- May need some text changes at short notice (anticipate 2 small updates to text)

Target Market(s)

Academics

Industry/Entity Type

Vextra

Font styles to use
Sans Serif

Colors

Designer to choose colors to be used in the design.

Requirements
Must have
• Don't look like powerpoint

```html
<!DOCTYPE html>
<html lang="en">
<head>
<meta charset="utf-8">
<title>Decreasing Language, Increasing Structure</title>
<link rel="stylesheet" href="https://fonts.googleapis.com/css2?family=Arimo:wght@400;700&display=swap">
<style>
  :root {
    --page: #ffffff;
    --panel: #f1f1f1;
    --label-border: #e6e6e6;
    --text-block: #55cfda;
    --text-rule: #ffffff;
    --data-block: #1a5479;
    --data-ink: #ffffff;
    --ink: #2f2f2f;
    --caption: #4b4b4b;
    --arrow-start: #4cc6d4;
    --arrow-end: #1a5479;
  }
  html, body {
    margin: 0;
    padding: 0;
    width: 1200px;
    height: 1200px;
    overflow: hidden;
    background: var(--page);
  }
  .figure { display: block; width: 1200px; height: 1200px; }
  .panel { fill: var(--panel); }
  .label-box { fill: var(--page); stroke: var(--label-border); stroke-width: 3; }
  .text-block { fill: var(--text-block); }
  .text-rule { stroke: var(--text-rule); stroke-width: 1.4; }
  .data-block { fill: var(--data-block); }
  .data-bits { fill: var(--data-ink); font-family: "Arimo", Arial, sans-serif; font-weight: 700; font-size: 13.5px; letter-spacing: 0.6px; }
  .slot-data { fill: none; stroke: var(--data-block); stroke-width: 1.5; stroke-dasharray: 5 4; }
  .slot-text { fill: none; stroke: var(--text-block); stroke-width: 1.5; stroke-dasharray: 5 4; }
  .label { fill: var(--ink); font-family: "Arimo", Arial, sans-serif; font-size: 20px; }
  .axis { stroke: url(#axisGradient); stroke-width: 3.5; fill: none; }
  .axis-head { stroke: var(--arrow-end); stroke-width: 3.5; fill: none; stroke-linecap: round; stroke-linejoin: round; }
  .axis-caption { fill: var(--caption); font-family: "Arimo", Arial, sans-serif; font-weight: 700; font-size: 26px; letter-spacing: 0.2px; }
</style>
</head>
<body>
<svg class="figure" viewBox="0 0 1500 1500" xmlns="http://www.w3.org/2000/svg" role="img" aria-label="Spectrum from text articles to structured statements">
  <defs>
    <linearGradient id="axisGradient" x1="43" y1="0" x2="1455" y2="0" gradientUnits="userSpaceOnUse">
      <stop offset="0" stop-color="var(--arrow-start)"/>
      <stop offset="0.55" stop-color="#3a9fc0"/>
      <stop offset="1" stop-color="var(--arrow-end)"/>
    </linearGradient>
  </defs>

  <!-- Stage 1: text article, no annotation -->
  <g class="stage">
    <rect class="panel" x="45" y="563" width="245" height="212"/>
    <rect class="label-box" x="46.5" y="774" width="242" height="77"/>
    <rect class="text-block" x="58" y="575" width="89" height="185"/>
    <g class="text-rule">
      <line x1="68" y1="588" x2="137" y2="588"/><line x1="68" y1="601.5" x2="137" y2="601.5"/>
      <line x1="68" y1="615" x2="137" y2="615"/><line x1="68" y1="628.5" x2="137" y2="628.5"/>
      <line x1="68" y1="642" x2="137" y2="642"/><line x1="68" y1="655.5" x2="137" y2="655.5"/>
      <line x1="68" y1="669" x2="137" y2="669"/><line x1="68" y1="682.5" x2="137" y2="682.5"/>
      <line x1="68" y1="696" x2="137" y2="696"/><line x1="68" y1="709.5" x2="137" y2="709.5"/>
      <line x1="68" y1="723" x2="137" y2="723"/><line x1="68" y1="736.5" x2="137" y2="736.5"/>
      <line x1="68" y1="750" x2="137" y2="750"/>
    </g>
    <rect class="slot-data" x="157" y="575" width="122" height="83"/>
    <text class="label" x="56" y="806">A text article</text>
    <text class="label" x="56" y="831">with no annotation data</text>
  </g>

  <!-- Stage 2: text article with annotation -->
  <g class="stage">
    <rect class="panel" x="332" y="563" width="245" height="212"/>
    <rect class="label-box" x="333.5" y="774" width="242" height="77"/>
    <rect class="text-block" x="345" y="575" width="89" height="185"/>
    <g class="text-rule">
      <line x1="355" y1="588" x2="424" y2="588"/><line x1="355" y1="601.5" x2="424" y2="601.5"/>
      <line x1="355" y1="615" x2="424" y2="615"/><line x1="355" y1="628.5" x2="424" y2="628.5"/>
      <line x1="355" y1="642" x2="424" y2="642"/><line x1="355" y1="655.5" x2="424" y2="655.5"/>
      <line x1="355" y1="669" x2="424" y2="669"/><line x1="355" y1="682.5" x2="424" y2="682.5"/>
      <line x1="355" y1="696" x2="424" y2="696"/><line x1="355" y1="709.5" x2="424" y2="709.5"/>
      <line x1="355" y1="723" x2="424" y2="723"/><line x1="355" y1="736.5" x2="424" y2="736.5"/>
      <line x1="355" y1="750" x2="424" y2="750"/>
    </g>
    <rect class="data-block" x="444" y="575" width="122" height="84"/>
    <text class="data-bits" x="453" y="593">101010110010</text>
    <text class="data-bits" x="453" y="613">111001100110</text>
    <text class="data-bits" x="453" y="633">000101101101</text>
    <text class="data-bits" x="453" y="653">10110</text>
    <text class="label" x="344" y="806">A text article</text>
    <text class="label" x="344" y="831">with annotation data</text>
  </g>

  <!-- Stage 3: paragraph-size texteme -->
  <g class="stage">
    <rect class="panel" x="621" y="617" width="245" height="158"/>
    <rect class="label-box" x="622.5" y="774" width="242" height="77"/>
    <rect class="text-block" x="634" y="629" width="89" height="134"/>
    <g class="text-rule">
      <line x1="644" y1="642" x2="713" y2="642"/><line x1="644" y1="655.5" x2="713" y2="655.5"/>
      <line x1="644" y1="669" x2="713" y2="669"/><line x1="644" y1="682.5" x2="713" y2="682.5"/>
      <line x1="644" y1="696" x2="713" y2="696"/><line x1="644" y1="709.5" x2="713" y2="709.5"/>
      <line x1="644" y1="723" x2="713" y2="723"/><line x1="644" y1="736.5" x2="713" y2="736.5"/>
      <line x1="644" y1="750" x2="713" y2="750"/>
    </g>
    <rect class="data-block" x="733" y="629" width="122" height="66"/>
    <text class="data-bits" x="742" y="647">101010110010</text>
    <text class="data-bits" x="742" y="667">111001100110</text>
    <text class="data-bits" x="742" y="687">000101101101</text>
    <text class="label" x="627" y="809">A paragraph-size texteme</text>
    <text class="label" x="627" y="835">with annotation data</text>
  </g>

  <!-- Stage 4: sentence-size micro-texteme -->
  <g class="stage">
    <rect class="panel" x="911" y="681" width="246" height="94"/>
    <rect class="label-box" x="912.5" y="774" width="243" height="77"/>
    <rect class="text-block" x="925" y="693" width="88" height="41"/>
    <g class="text-rule">
      <line x1="935" y1="707" x2="1003" y2="707"/>
      <line x1="935" y1="720" x2="1003" y2="720"/>
    </g>
    <rect class="data-block" x="1023" y="693" width="122" height="67"/>
    <text class="data-bits" x="1032" y="712">101010110010</text>
    <text class="data-bits" x="1032" y="732">111001100110</text>
    <text class="data-bits" x="1032" y="752">000101101101</text>
    <text class="label" x="925" y="796">A sentence-size</text>
    <text class="label" x="925" y="821">micro-texteme with</text>
    <text class="label" x="925" y="846">annotation data</text>
  </g>

  <!-- Stage 5: structured statement -->
  <g class="stage">
    <rect class="panel" x="1197" y="681" width="246" height="94"/>
    <rect class="label-box" x="1198.5" y="774" width="243" height="77"/>
    <rect class="slot-text" x="1210" y="693" width="90" height="67"/>
    <rect class="data-block" x="1310" y="693" width="122" height="67"/>
    <text class="data-bits" x="1319" y="712">101010110010</text>
    <text class="data-bits" x="1319" y="732">111001100110</text>
    <text class="data-bits" x="1319" y="752">000101101101</text>
    <text class="label" x="1209" y="809">A structured statement</text>
    <text class="label" x="1209" y="834">with no text</text>
  </g>

  <!-- Axis -->
  <line class="axis" x1="43" y1="888" x2="1452" y2="888"/>
  <polyline class="axis-head" points="1437,873 1454,888 1437,904"/>
  <text class="axis-caption" x="750" y="931" text-anchor="middle">DECREASING LANGUAGE | INCREASING STRUCTURE</text>
</svg>
</body>
</html>
```